Beautiful Upgraded Single Story Home in Avonlea...SOLD in 3 days for top $$!

This is a 6.5" x 11" QRVL postcard. Please use the indicia files and 6.5" x 11" template attached in the brief.

Reason: We are still working on the details for one of the postcards. Thanks

Target Market(s)

Listings

Font styles to use
Serif

Colors
33b8a4

Requirements
Must have
• Call me if you are interested in getting the most amount of equity out of your home!
• Marisol Denning (555) 814-3067 and Odile Pranwick (555) 372-9140
• Marisol@GroupPranwick.example and Odile@GroupPranwick.example
• Brightwater Properties
• The Key to your Real Estate Needs!
• (At bottom of postcard) "If you are currently listed with a licensed Realtor, this is not intended as solicitation"
Nice to have
• The Front Should be the Property Picture and "In Escrow in 3 Days!"

```html
<!DOCTYPE html>
<html lang="en">
<head>
<meta charset="utf-8">
<title>Sold in 3 Days – Postcard</title>
<link href="https://fonts.googleapis.com/css2?family=Roboto+Condensed:ital,wght@0,300;0,400;0,700;0,900;1,700;1,900&display=swap" rel="stylesheet">
<style>
  :root {
    --stage: #e9edf0;
    --forest: #0c5a45;
    --forest-light: #1d8c6c;
    --teal: #33b8a4;
    --teal-text: #2aa893;
    --red: #e8262a;
    --white: #ffffff;
    --ink: #1d2b2a;
    --grass: #6f9a3a;
    --suit: #2b2d30;
  }
  * { margin: 0; padding: 0; box-sizing: border-box; }
  html, body { width: 1200px; height: 1200px; overflow: hidden; }
  body {
    background: var(--stage);
    font-family: "Roboto Condensed", "Arial Narrow", sans-serif;
    position: relative;
  }
  .card {
    position: absolute;
    width: 479px;
    height: 862px;
    overflow: hidden;
    box-shadow: 0 6px 18px rgba(0,0,0,.18);
  }
  .card--front {
    left: 114px; top: 181px;
    background: linear-gradient(180deg, var(--forest) 0%, var(--forest-light) 55%);
  }
  .card--back { left: 654px; top: 218px; background: var(--white); }
  .abs { position: absolute; left: 0; width: 100%; text-align: center; }

  /* front */
  .front__photo {
    position: absolute; left: 0; top: 403px; width: 100%; bottom: 0;
    background: linear-gradient(180deg, #1f9a78 0%, #d9dcdc 30%, #f2f3f3 55%, var(--grass) 66%, #5d8a2e 100%);
  }
  .front__lead { top: 36px; color: var(--white); font-weight: 300; font-size: 50px; line-height: 1; }
  .front__days { top: 86px; color: var(--white); font-weight: 900; font-size: 80px; line-height: 1; }
  .front__sub { top: 170px; color: var(--white); font-weight: 400; font-size: 25px; line-height: 30px; text-transform: uppercase; }
  .front__sold { top: 262px; }
  .front__claim {
    top: 350px; color: var(--white); font-weight: 900; font-style: italic;
    font-size: 34px; transform: rotate(-8deg); letter-spacing: .5px;
  }
  .front__contact {
    top: 775px; color: var(--white); font-weight: 700; font-style: italic;
    font-size: 22px; line-height: 28px; text-transform: uppercase;
    text-shadow: 0 1px 2px rgba(0,0,0,.5);
  }

  .sold-graphic { display: block; width: 100%; height: 100px; }

  .brand-box {
    position: absolute; background: #efedea; border: 4px solid #111;
    outline: 3px solid var(--white);
    display: flex; align-items: center; justify-content: center; gap: 10px;
  }
  .brand-box__name { font-weight: 700; font-size: 24px; color: #111; line-height: 1.1; text-align: center; }
  .brand-box__mark { width: 18px; height: 18px; background: #111; flex: none; }
  .card--front .brand-box { left: 117px; top: 652px; width: 250px; height: 116px; }

  /* back */
  .back__photo {
    position: absolute; left: 150px; top: 90px; right: 0; height: 448px;
    background: linear-gradient(90deg, rgba(255,255,255,0) 0%, #4a4c50 35%, var(--suit) 70%, #3a3d42 100%);
  }
  .back__panel { position: absolute; left: 0; top: 538px; width: 100%; bottom: 0; background: var(--teal); }
  .back__lead { top: 36px; color: var(--teal-text); font-weight: 400; font-size: 33px; line-height: 1; }
  .back__lead strong { font-weight: 900; font-size: 46px; }
  .back__sold { top: 95px; }
  .card--back .brand-box { left: 114px; top: 486px; width: 248px; height: 112px; }
  .back__call {
    top: 648px; color: var(--white); font-weight: 700; font-size: 22px; line-height: 26px;
    text-transform: uppercase;
  }
  .back__contact { top: 734px; color: var(--white); font-weight: 400; font-size: 22px; line-height: 27px; text-transform: uppercase; }
  .back__note { top: 800px; color: var(--ink); font-weight: 700; font-size: 13px; line-height: 16px; text-transform: uppercase; }
</style>
</head>
<body>

<section class="card card--front">
  <div class="front__photo" role="img" aria-label="Photo of a white modern single story home on a green lawn"></div>
  <p class="abs front__lead">In Escrow in</p>
  <p class="abs front__days">3 DAYS!</p>
  <p class="abs front__sub">Beautiful upgraded<br>single story home<br>in Avonlea</p>
  <div class="abs front__sold">
    <svg class="sold-graphic" viewBox="0 0 479 100" aria-hidden="true">
      <g fill="var(--red)">
        <polygon points="0,55 110,45 110,55 0,65"/>
        <polygon points="0,70 110,60 110,68 0,78"/>
        <polygon points="380,35 479,26 479,36 380,45"/>
        <polygon points="380,49 479,40 479,49 380,58"/>
      </g>
      <text x="240" y="88" text-anchor="middle" transform="rotate(-5 240 60)"
            font-family="Roboto Condensed, sans-serif" font-weight="900" font-style="italic"
            font-size="100" fill="var(--red)" stroke="var(--white)" stroke-width="3" paint-order="stroke">SOLD</text>
    </svg>
  </div>
  <p class="abs front__claim">IN 3 DAYS FOR TOP $$!</p>
  <div class="brand-box">
    <span class="brand-box__mark"></span>
    <span class="brand-box__name">Brightwater<br>Properties</span>
  </div>
  <p class="abs front__contact">Marisol Denning (555) 814-3067<br>and Odile Pranwick (555) 372-9140</p>
</section>

<section class="card card--back">
  <div class="back__photo" role="img" aria-label="Photo of a businessman in a suit holding a small model house in his palm"></div>
  <div class="back__panel"></div>
  <p class="abs back__lead">In Escrow in <strong>3 DAYS!</strong></p>
  <div class="abs back__sold">
    <svg class="sold-graphic" viewBox="0 0 479 100" aria-hidden="true">
      <g fill="var(--red)">
        <polygon points="0,62 110,52 110,62 0,72"/>
        <polygon points="0,77 110,67 110,75 0,85"/>
        <polygon points="380,30 479,21 479,31 380,40"/>
        <polygon points="380,44 479,35 479,44 380,53"/>
      </g>
      <text x="245" y="90" text-anchor="middle" transform="rotate(-5 245 60)"
            font-family="Roboto Condensed, sans-serif" font-weight="900" font-style="italic"
            font-size="100" fill="var(--red)" stroke="var(--white)" stroke-width="3" paint-order="stroke">SOLD</text>
    </svg>
  </div>
  <svg style="position:absolute;left:160px;top:178px;width:260px;height:70px" viewBox="0 0 260 70" aria-hidden="true">
    <text x="130" y="50" text-anchor="middle" transform="rotate(-8 130 40)"
          font-family="Roboto Condensed, sans-serif" font-weight="900" font-style="italic"
          font-size="36" fill="var(--white)" stroke="var(--teal-text)" stroke-width="3" paint-order="stroke">FOR TOP $$!</text>
  </svg>
  <div class="brand-box">
    <span class="brand-box__mark"></span>
    <span class="brand-box__name">Brightwater<br>Properties</span>
  </div>
  <p class="abs back__call">Call me if you are interested in<br>getting the most amount of<br>equity out of your home!</p>
  <p class="abs back__contact">Marisol Denning (555) 814-3067<br>and Odile Pranwick (555) 372-9140</p>
  <p class="abs back__note">If you are currently listed with a licensed Realtor,<br>this is not intended as solicitation"</p>
</section>

</body>
</html>
```